CRPG is needing business cards, and stationary created.

Pixel Forge created a logo for our business, and now we are wanting business cards, and stationary. I have included two designs of the same logo. Please feel free to use them as you want. The name of the company is Cedar Ridge Property Group LLC, the address is 812 NE Willow Ln., Suite 9, the city & state is Pine Falls, Idaho, zip code is 97815, Telephone number is 541-327-4489, Fax number is 541-327-6051, the name on the business card is Carl Whitby CMCA

Industry/Entity Type

Property Management

Contact Information for Business Card

The card needs to look professional. Upscale.

Requirements
Must have
• The colors we are using are on the logo that has been uploaded.

```html
<!DOCTYPE html>
<html lang="en">
<head>
<meta charset="utf-8">
<title>Cedar Ridge Property Group — Business Card</title>
<link rel="stylesheet" href="https://fonts.googleapis.com/css2?family=Exo+2:wght@600;700&family=Open+Sans:wght@400&display=swap">
<style>
  :root {
    --green: #178c78;
    --slate: #3d4a5a;
    --ink: #2f3640;
    --white: #ffffff;
    --rule: #c4c6c9;
    --bg-light: #dcdddf;
    --bg-dark: #8d8e92;
  }
  * { margin: 0; padding: 0; box-sizing: border-box; }
  html, body { width: 1200px; height: 1119px; overflow: hidden; }
  body {
    position: relative;
    background: linear-gradient(100deg, var(--bg-light) 0%, #b9babd 55%, var(--bg-dark) 100%);
    font-family: "Open Sans", sans-serif;
  }
  .card-wrap { position: absolute; filter: drop-shadow(0 2px 4px rgba(0,0,0,0.25)); }
  .card {
    position: relative;
    width: 782px;
    height: 447px;
    clip-path: polygon(99px 0, 683px 0, 782px 79px, 782px 368px, 683px 447px, 99px 447px, 0 368px, 0 79px);
  }
  .card--front { background: var(--white); }
  .card--back { background: var(--slate); }
  .front-wrap { left: 101px; top: 75px; }
  .back-wrap { left: 323px; top: 594px; }

  .brand-name {
    position: absolute;
    font-family: "Exo 2", sans-serif;
    font-weight: 700;
    text-transform: uppercase;
    line-height: 1.05;
    display: flex;
    align-items: center;
    gap: 16px;
  }
  .brand-mark { width: 22px; height: 22px; flex: none; }
  .card--front .brand-name { left: 58px; top: 175px; color: var(--green); font-size: 40px; }
  .card--front .brand-mark { background: var(--slate); }
  .card--back .brand-name { left: 130px; top: 168px; color: var(--white); font-size: 48px; }
  .card--back .brand-mark { background: var(--white); }

  .divider { position: absolute; left: 450px; top: 84px; width: 2px; height: 277px; background: var(--rule); }

  .person { position: absolute; left: 481px; top: 84px; font-family: "Exo 2", sans-serif; font-weight: 600; }
  .person-name { color: var(--slate); font-size: 28px; letter-spacing: 0.5px; line-height: 32px; }
  .person-title { color: var(--green); font-size: 26px; line-height: 32px; }

  .contact-list { position: absolute; left: 482px; top: 163px; list-style: none; color: var(--ink); font-size: 20px; }
  .contact-list li { display: flex; align-items: center; height: 33px; }
  .contact-list svg { width: 20px; height: 18px; margin-right: 11px; fill: var(--slate); }

  .address { position: absolute; left: 482px; top: 279px; color: var(--ink); font-size: 20px; line-height: 30px; font-style: normal; }

  .website {
    position: absolute; left: 0; right: 0; top: 392px;
    text-align: center; color: var(--white); font-size: 26px; letter-spacing: 4px;
  }
</style>
</head>
<body>
  <div class="card-wrap front-wrap">
    <section class="card card--front">
      <div class="brand-name"><span class="brand-mark"></span><span>Cedar Ridge<br>Property Group</span></div>
      <div class="divider"></div>
      <div class="person">
        <div class="person-name">CARL WHITBY</div>
        <div class="person-title">CMCA</div>
      </div>
      <ul class="contact-list">
        <li><svg viewBox="0 0 20 18"><path d="M4 1l3 3-2 2c1 3 4 6 7 7l2-2 3 3-2 3C8 16 2 10 1 3z"/></svg>541-327-4489</li>
        <li><svg viewBox="0 0 20 18"><path d="M5 1h9v5H5z M2 7h16v8H2z M6 11h8v6H6z"/></svg>541-327-6051</li>
        <li><svg viewBox="0 0 20 18"><path d="M1 6l9-5 9 5v11H1z M3 7l7 5 7-5"/></svg>info@cedarridgepg.com</li>
      </ul>
      <address class="address">812 NE Willow Ln., Suite 9<br>the city &amp; state is Pine Falls<br>Idaho, zip code is 97815</address>
    </section>
  </div>

  <div class="card-wrap back-wrap">
    <section class="card card--back">
      <div class="brand-name"><span class="brand-mark"></span><span>Cedar Ridge<br>Property Group</span></div>
      <div class="website">www.cedarridgepg.com</div>
    </section>
  </div>
</body>
</html>
```